Plumber needs a business card

I need a new business card for my plumbing business. I dont have a logo at the moment but I want business cards that are simple but very professional. I want to look like
Name: Milo Brenton
Address: (just make one up)
Phone: 0497 318 264
Email: milo@fernpost.net
Colors to use:
Blacks, blues, silvers

```html
<!DOCTYPE html>
<html lang="en">
<head>
<meta charset="utf-8">
<title>Milo Brenton – Business Card</title>
<link rel="stylesheet" href="https://fonts.googleapis.com/css2?family=Lato:wght@400;700&display=swap">
<style>
  :root {
    --page-bg: #e9eaec;
    --card-black: #1d1d1f;
    --card-grain: #252527;
    --band-silver: #c9c9cb;
    --name-ink: #161616;
    --detail-ink: #d6d6d8;
    --rule-silver: #a8a8ab;
  }
  * { box-sizing: border-box; margin: 0; padding: 0; }
  html, body {
    width: 1200px;
    height: 750px;
    overflow: hidden;
    background: var(--page-bg);
    font-family: "Lato", Arial, sans-serif;
  }
  .stage {
    width: 1200px;
    height: 750px;
    display: flex;
    align-items: center;
    justify-content: center;
  }
  .business-card {
    position: relative;
    width: 840px;
    height: 480px;
    background-color: var(--card-black);
    background-image:
      radial-gradient(circle at 30% 40%, var(--card-grain) 0 1px, transparent 1.5px),
      radial-gradient(circle at 70% 70%, var(--card-grain) 0 1px, transparent 1.5px);
    background-size: 6px 6px, 7px 7px;
    box-shadow: 0 14px 30px rgba(0, 0, 0, 0.28);
    overflow: hidden;
  }
  .name-band {
    position: absolute;
    left: 0;
    top: 272px;
    width: 380px;
    height: 66px;
    background: var(--band-silver);
    display: flex;
    align-items: center;
    justify-content: flex-end;
    padding-right: 46px;
  }
  .holder-name {
    font-weight: 700;
    font-size: 34px;
    color: var(--name-ink);
    letter-spacing: 0.2px;
  }
  .divider {
    position: absolute;
    left: 446px;
    top: 128px;
    width: 2px;
    height: 126px;
    background: var(--rule-silver);
  }
  .contact-block {
    position: absolute;
    left: 492px;
    top: 104px;
    color: var(--detail-ink);
    font-size: 17px;
    line-height: 1.3;
  }
  .address { margin-bottom: 28px; }
  .contact-line {
    display: flex;
    align-items: center;
    gap: 10px;
    font-size: 18px;
  }
  .contact-icon {
    width: 17px;
    height: 17px;
    flex: none;
  }
</style>
</head>
<body>
  <main class="stage">
    <article class="business-card">
      <div class="name-band">
        <h1 class="holder-name">Milo Brenton</h1>
      </div>

      <div class="divider" aria-hidden="true"></div>

      <section class="contact-block">
        <p class="address">fenwick mill road<br>harlow park,ashby</p>
        <p class="contact-line">
          <svg class="contact-icon" viewBox="0 0 16 16" aria-hidden="true">
            <rect x="4" y="1" width="8" height="14" rx="1.5" fill="none" stroke="currentColor" stroke-width="1.3"/>
            <line x1="7" y1="12.6" x2="9" y2="12.6" stroke="currentColor" stroke-width="1.3"/>
          </svg>
          <span>0497 318 264</span>
        </p>
        <p class="contact-line">
          <svg class="contact-icon" viewBox="0 0 16 16" aria-hidden="true">
            <rect x="1" y="3" width="14" height="10" fill="currentColor"/>
            <polyline points="1,3 8,9 15,3" fill="none" stroke="#1d1d1f" stroke-width="1.2"/>
          </svg>
          <span>milo@fernpost.net</span>
        </p>
      </section>
    </article>
  </main>
</body>
</html>
```